Raw Material for Personal Care Products

We need to make a brochure with the products we sell to manufacture natural personal care products

Target Market(s)

Cosmetics Manufacturers

Industry/Entity Type

Cosmetics

Colors
00AB8E
00BBA5
67D7C9
C6EFE9
E9F9F6

Requirements
Must have
• Images associated with nature, organics
Should not have
• Chemicals industries, refinaries

```html
<!DOCTYPE html>
<html lang="es">
<head>
<meta charset="utf-8">
<title>Materias Primas Naturales – Nativa Química</title>
<link rel="stylesheet" href="https://fonts.googleapis.com/css2?family=Cormorant+Garamond:wght@400;500&family=Libre+Caslon+Text:wght@400;700&display=swap">
<style>
  :root{
    --backdrop:#ececec;
    --paper:#ffffff;
    --teal:#4fa38e;
    --teal-text:#2f9c83;
    --olive:#7f8c3c;
    --olive-text:#7d8c3c;
    --ink:#1d1d1b;
    --white:#ffffff;
  }
  html,body{margin:0;padding:0;width:1200px;height:1200px;overflow:hidden;background:var(--backdrop);}
  .flyer{
    position:absolute;left:163px;top:34px;width:1267px;height:1641px;
    background:var(--paper);transform:scale(.69);transform-origin:0 0;overflow:hidden;
    font-family:"Libre Caslon Text",Georgia,serif;color:var(--ink);
  }
  .photo{position:absolute;border-radius:50%;}
  .photo--hero{left:-50px;top:-280px;width:880px;height:880px;
    background:radial-gradient(circle at 55% 70%,#f2a08f 0%,#e9b3a6 30%,#ebe3e0 60%,#e6e4e4 100%);}
  .photo--water{left:555px;top:195px;width:400px;height:400px;border:6px solid var(--white);box-sizing:border-box;
    background:radial-gradient(circle at 40% 35%,#cfe1c4 0%,#b5cfa9 55%,#e8ebe5 100%);}
  .photo--oil{left:70px;top:610px;width:230px;height:230px;background:radial-gradient(circle at 45% 45%,#f5efe6 0%,#e8dccb 60%,#c9a78a 100%);}
  .photo--pour{left:732px;top:613px;width:230px;height:230px;border:4px solid var(--white);background:radial-gradient(circle at 50% 55%,#e8e2dc 0%,#c9bcb1 55%,#9e8d7f 100%);z-index:2;}
  .photo--scent{left:72px;top:1332px;width:230px;height:230px;background:radial-gradient(circle at 40% 50%,#e7e8ea 0%,#a9acbd 50%,#7f829b 100%);}

  .title-band{position:absolute;left:455px;top:81px;width:812px;height:231px;background:var(--teal);border-radius:62px 0 0 62px;color:var(--white);}
  .title-band h1{margin:0;position:absolute;left:80px;top:30px;font-family:"Cormorant Garamond",Georgia,serif;font-weight:500;font-size:52px;line-height:64px;white-space:nowrap;}
  .contact{position:absolute;left:80px;top:178px;font-family:"Cormorant Garamond",Georgia,serif;font-weight:500;font-size:28px;white-space:nowrap;}
  .contact .sep{margin:0 28px;}

  .brand{position:absolute;left:1040px;top:380px;width:200px;text-align:center;font-family:"Libre Caslon Text",Georgia,serif;font-weight:700;color:var(--ink);}
  .brand .mark{width:60px;height:60px;background:var(--teal);margin:0 auto 14px;}
  .brand .name{font-size:38px;line-height:40px;letter-spacing:1px;}
  .brand .sub{font-size:20px;letter-spacing:10px;line-height:28px;}

  .section-head{position:absolute;margin:0;font-weight:400;font-size:30px;line-height:37px;}
  .head--oils{left:335px;top:660px;color:var(--olive-text);}
  .head--surf{left:990px;top:697px;color:var(--white);z-index:3;}
  .head--scent{left:357px;top:1395px;color:var(--teal-text);}

  .list{position:absolute;margin:0;padding:0;list-style:none;font-size:21px;line-height:27.3px;white-space:nowrap;}
  .list li{position:relative;padding-left:23px;}
  .list li::before{content:"";position:absolute;left:0;top:11px;width:6px;height:6px;border-radius:50%;background:currentColor;}
  .list--oils li::before{background:var(--olive);}
  .list--oils-a{left:75px;top:890px;}
  .list--oils-b{left:375px;top:890px;}

  .surf-panel{position:absolute;left:712px;top:612px;width:555px;height:825px;background:var(--olive);
    clip-path:path("M218 0 H555 V825 H40 Q0 825 0 785 V218 Z");color:var(--white);}
  .surf-panel h3{position:absolute;margin:0;left:21px;font-weight:400;font-size:23px;line-height:30px;}
  .sub--amino{top:264px;}
  .sub--glu{top:516px;}
  .surf-panel .list{left:25px;}
  .list--amino{top:336px;}
  .list--glu{top:588px;}

  .scent-lines{position:absolute;left:357px;top:1433px;margin:0;font-size:23px;line-height:30px;}

  .certs{position:absolute;left:735px;top:1478px;}
  .certs svg{position:absolute;left:0;top:0;}
  .certs ul{position:absolute;left:92px;top:-6px;margin:0;padding:0;list-style:none;font-size:17px;line-height:22px;white-space:nowrap;text-transform:uppercase;}
</style>
</head>
<body>
<main class="flyer">
  <div class="photo photo--hero" role="img" aria-label="Frasco gotero ámbar sobre pétalos de rosa en bandeja de madera"></div>
  <div class="photo photo--water" role="img" aria-label="Cuenco con agua y rodajas de limón junto a flores blancas"></div>

  <header class="title-band">
    <h1>Materias Primas Naturales<br>Orgánicas para Cuidado Personal</h1>
    <div class="contact">+000 000 000<span class="sep">|</span>www.web.com</div>
  </header>

  <div class="brand">
    <div class="mark"></div>
    <div class="name">NATIVA</div>
    <div class="sub">QUIMICA</div>
  </div>

  <div class="photo photo--oil" role="img" aria-label="Manos sosteniendo un platillo con aceite natural"></div>
  <h2 class="section-head head--oils">ACEITES Y<br>MANTECAS<br>NATURALES</h2>

  <ul class="list list--oils list--oils-a">
    <li>Aceite de Acaí</li><li>Aceite de Aguacate</li><li>Aceite de Almendra Dulce</li><li>Aceite de Andiroba</li>
    <li>Aceite de Argán</li><li>Aceite de Avellana</li><li>Aceite de Babacu</li><li>Aceite de Buriti</li>
    <li>Aceite de Castor</li><li>Aceite de Coco</li><li>Aceite de de Nuez</li><li>Aceite de Girasol</li>
    <li>Aceite de Jojoba</li><li>Aceite de Macadamia</li>
  </ul>
  <ul class="list list--oils list--oils-b">
    <li>Aceite de Oliva</li><li>Aceite de Pracaxi</li><li>Aceite de Semilla de Durazno</li><li>Aceite de Semilla de Uva</li>
    <li>Aceite de Sesamo</li><li>Aceite de Soya</li><li>Aceite de Zanahoria</li><li>Manteca de Cupuacu</li>
    <li>Manteca de Karite</li><li>Manteca de Murumuru</li><li>Manteca de Ucuba</li><li>Scrub de Murumuru</li>
  </ul>

  <section class="surf-panel">
    <h3 class="sub--amino">SURFACTANTE<br>AMINO ACIDO</h3>
    <ul class="list list--amino">
      <li>Glicinato de Potasio Cocoil y Glicerina.</li><li>Glicinato de Potasio Cocoil</li>
      <li>Glicinato de Sodio Cocoil y Glicerina.</li><li>Glicinato de Sodio Cocoil</li><li>Glutamato de Sodio Cocoil</li>
    </ul>
    <h3 class="sub--glu">SUFACTANTE ALQUIL<br>GLUCOSIDO.</h3>
    <ul class="list list--glu">
      <li>Glucosido Laurico</li><li>Glucosido de Coco</li><li>Glucosido Decilico</li>
      <li>Hidroxipropil Sulfonato Laurilglucosido de Sodio</li>
      <li>Carboxilato Glucosa Laurico de Sodio y<br>Glucosido Laurico.</li>
      <li>Cocoil Isetianato de Sodio (SCI)</li><li>CocoamidoPropilBetaine (CAPB)</li>
    </ul>
  </section>
  <div class="photo photo--pour" role="img" aria-label="Mano vertiendo un líquido transparente desde un vaso"></div>
  <h2 class="section-head head--surf">SURFACTANTES<br>NATURALES</h2>

  <div class="photo photo--scent" role="img" aria-label="Frasco de fragancia con flores de lavanda secas"></div>
  <h2 class="section-head head--scent">FRAGANCIAS</h2>
  <p class="scent-lines">Fragancias Convencionales<br>Fragancias Naturales<br>100% (VERDEFLOR)</p>

  <div class="certs">
    <svg width="76" height="92" viewBox="0 0 76 92" aria-hidden="true">
      <path d="M38 4 L70 16 V44 C70 64 56 80 38 88 C20 80 6 64 6 44 V16 Z" fill="none" stroke="var(--olive)" stroke-width="6" stroke-linejoin="round"/>
      <path d="M24 46 L34 56 L52 36" fill="none" stroke="var(--olive)" stroke-width="6" stroke-linecap="round" stroke-linejoin="round"/>
    </svg>
    <ul>
      <li>Certificaciones</li>
      <li>Ecoverde (Organic Farming Product)</li>
      <li>Cosmia Organic</li>
      <li>Kosher (Kashrut Council)</li>
      <li>Agro Organic</li>
    </ul>
  </div>
</main>
</body>
</html>
```